Real Estate Graphics and Ad Redesign - Digital Marketing Assets

I am looking for someone to create a variety of custom graphics for our company and redesign some of our existing ads and digital marketing material. Please see attached. Look for redesign of graphics and chart to look good and clear and clean.

Target Market(s)

Real Estate Lead generation, mortgage lenders and Business 2 Business Sales

Industry/Entity Type

Real Estate

Font styles to use
Serif
Sans Serif

Colors
f78f20
33a6d7
0a91cc
fac994
fff5ef
cee9f5
b868aa
add136
e667a6

Requirements
Must have
• Must be clean, easy to understand, friendly and custom look and feel. I like the concept of future and tech but at the same time elegant and well thought out. The idea is that the concepts we are explaining and what we are doing is somewhat complex and thus clarity and appeal are required.
Nice to have
• Custom graphics and visual representations of texts
Should not have
• Complicated or hard to digest layout. Overly busy and hard colors, it should be sleek, easy to digest.

```html
<!DOCTYPE html>
<html lang="en">
<head>
<meta charset="utf-8">
<title>Nestwise Marketing Slides</title>
<link href="https://fonts.googleapis.com/css2?family=Montserrat:wght@600;700&family=Open+Sans:wght@400;600&display=swap" rel="stylesheet">
<style>
:root{
  --orange:#ff4a14;
  --peach:#f9a98a;
  --blush:#fbf1ec;
  --purple:#8a2be2;
  --blue:#1e9be9;
  --navy:#0b4f7a;
  --brown:#8b2a0e;
  --slate:#5f6475;
  --ink:#1b1b24;
  --mist:#cdd3dc;
  --sky:#dff0fb;
  --gold:#d9a43a;
  --white:#ffffff;
}
*{box-sizing:border-box;margin:0;padding:0}
html,body{width:1200px;height:1200px;overflow:hidden;background:var(--white)}
body{position:relative;font-family:"Open Sans",sans-serif;color:var(--ink)}
.slide{position:absolute;width:563px;height:317px;overflow:hidden;background:var(--white);box-shadow:0 4px 10px rgba(0,0,0,.18)}
.slide-overview{left:33px;top:86px;background:var(--blush)}
.slide-leads{left:611px;top:86px}
.slide-transaction{left:33px;top:446px;background:#f7f8fa}
.slide-partnership{left:611px;top:446px;background:#f6f7f9}
.slide-summary{left:323px;top:805px}
.deco{position:absolute;left:0;top:0}
.brand{position:absolute;font-family:"Montserrat",sans-serif;font-weight:700;white-space:nowrap}
.brand-direct{color:var(--purple)}
.brand-connect{color:var(--blue)}
.brand-protect{color:var(--orange)}
.brand-select{color:var(--blue)}
.brand-dot{display:inline-block;width:.55em;height:.55em;border-radius:50%;background:currentColor;margin-right:.3em;vertical-align:.05em}
/* overview cards */
.service-card{position:absolute;top:46px;width:122px;height:251px;background:var(--white);border-radius:14px;padding:14px 9px 0}
.service-card h3{font-family:"Montserrat",sans-serif;font-weight:700;font-size:7px;line-height:1.25;text-align:center;padding-bottom:6px;border-bottom:1px solid #ddd;margin-bottom:8px}
.service-card p,.service-card li{font-size:5.3px;line-height:1.35}
.service-card p{margin-bottom:5px}
.service-card ul{list-style:none;margin-bottom:5px}
.service-card ul.sub{padding-left:6px;margin-bottom:0}
.service-card b{font-weight:600}
.card-direct h3{color:var(--purple)}
.card-connect h3{color:var(--blue)}
.card-protect h3{color:var(--orange)}
.card-select h3{color:var(--ink)}
/* shared */
.filled-art{position:absolute}
.browser{position:absolute;background:#e9ebef;border-radius:5px;overflow:hidden}
.browser-bar{height:16px;display:flex;align-items:center;padding-left:6px;gap:3px}
.browser-bar i{width:4px;height:4px;border-radius:50%;display:block}
.browser-url{position:absolute;left:18px;top:12px;right:6px;height:9px;background:var(--white);border-radius:4px;font-size:4.5px;line-height:9px;padding-left:5px;color:#555}
.browser-map{position:absolute;left:0;right:0;bottom:0;background:linear-gradient(135deg,#e4e8e2,#d9dfe6 55%,#f1e7cf)}
.slide-title{font-family:"Montserrat",sans-serif;font-weight:700}
.bullets{list-style:none;position:absolute}
.bullets li{position:relative;padding-left:10px}
.bullets li::before{content:"";position:absolute;left:0;width:4px;height:4px;border-radius:50%;background:var(--bullet,var(--orange))}
/* leads */
.lead-card{position:absolute;left:262px;top:74px;width:276px;height:165px;background:var(--white);border-radius:10px;box-shadow:0 3px 12px rgba(0,0,0,.08)}
.lead-card .bullets{left:10px;top:10px;right:6px;font-size:9.3px;line-height:11.3px}
.lead-card .bullets li{margin-bottom:5px}
.lead-card .bullets li::before{top:4px}
.lead-card .bullets li:nth-child(odd){--bullet:var(--purple)}
/* transaction */
.slide-transaction .bullets{left:239px;top:104px;width:312px;font-size:8.1px;line-height:9.6px}
.slide-transaction .bullets li{margin-bottom:9px}
.slide-transaction .bullets li::before{top:3px;width:3px;height:3px}
.slide-transaction .bullets li.sub{margin-left:8px;--bullet:var(--blue)}
.chart-label{font-family:"Open Sans",sans-serif}
/* partnership */
.slide-partnership .bullets{left:57px;top:106px;width:255px;font-size:9.2px;line-height:11px}
.slide-partnership .bullets li{margin-bottom:10px}
.slide-partnership .bullets li::before{top:4px}
/* summary */
.summary-title{position:absolute;left:0;right:0;top:200px;text-align:center;font-size:12px;padding-left:-1px}
.summary-list{position:absolute;left:131px;top:218px;list-style:none;font-size:8.6px;line-height:11.4px}
.summary-list li::before{content:"• "}
</style>
</head>
<body>

<!-- Slide: service overview -->
<section class="slide slide-overview">
  <svg class="deco" width="563" height="317" viewBox="0 0 563 317">
    <path d="M563 0 L563 317 L0 317 L0 250 C60 260 120 300 230 250 C330 205 420 260 470 200 C520 140 540 60 563 0Z" fill="var(--orange)"/>
    <path d="M563 0 C540 70 520 140 470 200 C430 250 380 230 330 240 L563 240Z" fill="var(--peach)" opacity=".8"/>
  </svg>
  <div class="brand brand-direct" style="left:42px;top:26px;font-size:12px"><span class="brand-dot"></span>Nestwise Direct</div>
  <div class="brand brand-connect" style="left:175px;top:27px;font-size:10.5px">Nestwise Connect</div>
  <div class="brand brand-protect" style="left:312px;top:27px;font-size:10.5px">Nestwise Protect</div>
  <div class="brand brand-select" style="left:447px;top:27px;font-size:10.5px">Nestwise Select</div>

  <article class="service-card card-direct" style="left:20px">
    <h3>Lead Generation &amp;<br>Conversion</h3>
    <p>• 90% of buyers start online when home shopping.<br>• 81% of buyers do not have agents when getting pre-approved for a loan.<br>• NW Direct Generates and purchases Lender Exclusive and Realtor Exclusive leads.</p>
    <p><b>Support:</b></p>
    <ul><li>• MLS Integration</li><li>• Lead Captures</li><li>• Buyer Engagement Strategy Team (B.E.S.T.)</li>
      <li><ul class="sub"><li>• Text message</li><li>• Email o Calls</li><li>• Drip Campaigns</li><li>• Lead Management</li></ul></li></ul>
    <p><b>NW Lead Purchases</b><br>• Purchase Pre-qualified Buyer Leads from lenders.<br>• We buy leads from lender of pre-qualified buyers without agents</p>
  </article>

  <article class="service-card card-connect" style="left:154px">
    <h3>Transaction Management<br>System</h3>
    <p>• NW Manages the transaction from initial lead generation to pre-approval, home shopping and final closing.</p>
    <p><b>Transaction Management System</b></p>
    <ul class="sub"><li>• Deal Tracking</li><li>• Bi-weekly Updates</li><li>• Agent Assignment</li><li>• Follow-up Dates</li><li>• Stage and Substage Management</li></ul>
    <p style="margin-top:5px">NW Select Preferred Service Provider Network.</p>
    <p>NW Protect - 2 Year protection and service level agreement.</p>
    <p>LOS and POS Integrations</p>
    <p>B.E.S.T.</p>
  </article>

  <article class="service-card card-protect" style="left:288px">
    <h3>Buyer Engagement &amp;<br>Transaction Management</h3>
    <p>• NW ensure the lender originally assigned to the buyer and realtor will remain in contact and engaged.</p>
    <p>• NW - 2 Year Protection and Realtor SLA</p>
    <p>• Realtor Coaching</p>
    <p style="margin-bottom:0">• B.E.S.T Follow-up</p>
    <ul class="sub"><li>• Buyer</li><li>• Engagement</li><li>• Strategy</li><li>• Team</li></ul>
    <p style="margin-top:5px">• File Stage and Substage Management</p>
    <p>• Buyer Concierge Service</p>
    <p>• Buyer Education</p>
    <p>• Social Media and retargeting</p>
  </article>

  <article class="service-card card-select" style="left:422px">
    <h3>Preferred Service<br>Provider Network</h3>
    <p>• Realtor Panel Management System.</p>
    <p>• Hyper-Local Real Estate Agent Assignment.</p>
    <p>• NW Crew - Nationwide Real Estate Network.</p>
    <p>• Set-up preferred agent panels.</p>
    <p>• Leads assigned by zip code and coverage area.</p>
    <p>• No Fee for joining network.</p>
    <p>• Lenders can set-up exclusive Realtor panels.</p>
    <p>• Success based broker to broker referral agreement.</p>
    <p>• No cost to lenders.</p>
  </article>
</section>

<!-- Slide: lead generation -->
<section class="slide slide-leads">
  <svg class="deco" width="563" height="317" viewBox="0 0 563 317">
    <path d="M0 190 C40 170 90 180 100 230 C110 270 170 250 230 270 C280 285 225 317 225 317 L0 317Z" fill="var(--purple)"/>
    <path d="M0 280 C40 230 110 240 180 280 C240 310 280 260 265 317" fill="none" stroke="var(--orange)" stroke-width="1.5"/>
    <path d="M500 0 L563 0 L563 40 C545 30 520 35 500 20 C492 12 494 4 500 0Z" fill="var(--purple)"/>
    <path d="M60 10 C150 60 300 -10 420 40" fill="none" stroke="#f6d9cf" stroke-width="1"/>
    <ellipse cx="135" cy="250" rx="100" ry="3" fill="#d6d6d6"/>
  </svg>
  <div class="brand brand-direct" style="left:37px;top:40px;font-size:17px"><span class="brand-dot"></span>Nestwise Direct</div>
  <h2 class="slide-title" style="position:absolute;left:270px;top:40px;font-size:22px">Lead Generation</h2>
  <div class="browser" style="left:37px;top:82px;width:197px;height:144px">
    <div class="browser-bar"><i style="background:var(--purple)"></i><i style="background:var(--orange)"></i><i style="background:var(--blue)"></i></div>
    <div class="browser-url">https://www.nestwiserealty.com/direct/</div>
    <div class="browser-map" style="top:22px" role="img" aria-label="Home search map with listing price pins and a sign-in panel"></div>
  </div>
  <div class="lead-card">
    <ul class="bullets">
      <li>NW uses online ads to attract qualified buyers</li>
      <li>NW uses MLS and local housing information to convert buyers to qualified leads and captures their information</li>
      <li>NW uses best practices in lead conversion strategies to maintain the buyer relationship and convert the buyers</li>
      <li>NW assigns its buyers to hyper local qualified agents who begin the homebuying process</li>
      <li>NW partners with the best lenders to facilitate the pre-approval and funding of the purchase</li>
    </ul>
  </div>
  <div class="filled-art" style="left:414px;top:228px;width:130px;height:82px;background:linear-gradient(90deg,#fbe3da,#e6eef8)" role="img" aria-label="Illustration of two business people presenting a growth chart"></div>
</section>

<!-- Slide: transaction management -->
<section class="slide slide-transaction">
  <svg class="deco" width="563" height="317" viewBox="0 0 563 317">
    <g fill="#e6f3fb"><circle cx="205" cy="95" r="17"/><circle cx="222" cy="268" r="22"/><circle cx="503" cy="268" r="38"/><circle cx="353" cy="293" r="13"/><circle cx="40" cy="255" r="18"/><circle cx="45" cy="90" r="18"/></g>
    <g stroke="#e6f3fb" stroke-width="3"><line x1="205" y1="95" x2="150" y2="190"/><line x1="160" y1="217" x2="222" y2="268"/></g>
    <!-- small donut -->
    <g transform="rotate(-90 94 137)" fill="none" stroke-width="9">
      <circle cx="94" cy="137" r="22" pathLength="100" stroke="var(--orange)" stroke-dasharray="18 100"/>
      <circle cx="94" cy="137" r="22" pathLength="100" stroke="var(--navy)" stroke-dasharray="32 100" stroke-dashoffset="-18"/>
      <circle cx="94" cy="137" r="22" pathLength="100" stroke="var(--brown)" stroke-dasharray="5 100" stroke-dashoffset="-50"/>
      <circle cx="94" cy="137" r="22" pathLength="100" stroke="var(--slate)" stroke-dasharray="25 100" stroke-dashoffset="-55"/>
      <circle cx="94" cy="137" r="22" pathLength="100" stroke="var(--blue)" stroke-dasharray="20 100" stroke-dashoffset="-80"/>
    </g>
    <!-- large donut -->
    <g transform="rotate(-90 160 217)" fill="none" stroke-width="16">
      <circle cx="160" cy="217" r="36" pathLength="100" stroke="var(--blue)" stroke-dasharray="10 100"/>
      <circle cx="160" cy="217" r="36" pathLength="100" stroke="var(--orange)" stroke-dasharray="4 100" stroke-dashoffset="-10"/>
      <circle cx="160" cy="217" r="36" pathLength="100" stroke="var(--navy)" stroke-dasharray="28 100" stroke-dashoffset="-14"/>
      <circle cx="160" cy="217" r="36" pathLength="100" stroke="var(--slate)" stroke-dasharray="20 100" stroke-dashoffset="-42"/>
      <circle cx="160" cy="217" r="36" pathLength="100" stroke="var(--brown)" stroke-dasharray="18 100" stroke-dashoffset="-62"/>
      <circle cx="160" cy="217" r="36" pathLength="100" stroke="var(--blue)" stroke-dasharray="20 100" stroke-dashoffset="-80"/>
    </g>
    <g stroke="var(--slate)" stroke-width=".6" fill="none">
      <polyline points="48,106 78,106 88,118"/><polyline points="148,99 120,99 112,117"/><polyline points="155,147 130,147 118,152"/><polyline points="48,164 70,164 82,156"/>
      <polyline points="128,180 100,180 95,160"/><polyline points="220,174 195,174 185,190"/><polyline points="70,196 100,196 128,200"/><polyline points="248,235 222,235 200,225"/>
      <polyline points="85,265 112,265 128,245"/><polyline points="198,280 168,280 160,256"/>
    </g>
    <g class="chart-label" font-size="6.5" font-weight="600">
      <text x="45" y="97" fill="var(--ink)" font-weight="400">xx %</text><text x="45" y="105" fill="var(--blue)">Data 1</text>
      <text x="110" y="93" fill="var(--ink)" font-weight="400">xx %</text><text x="110" y="101" fill="var(--orange)">Data 2</text>
      <text x="132" y="139" fill="var(--ink)" font-weight="400">xx %</text><text x="132" y="147" fill="var(--navy)">Data 4</text>
      <text x="42" y="155" fill="var(--ink)" font-weight="400">xx %</text><text x="42" y="163" fill="var(--slate)">Data 3</text>
      <text x="104" y="172" fill="var(--ink)" font-weight="400">xx %</text><text x="104" y="180" fill="var(--brown)">Data 5</text>
      <text x="197" y="166" fill="var(--ink)" font-weight="400">xx %</text><text x="197" y="174" fill="var(--orange)">Data 2</text>
      <text x="70" y="187" fill="var(--ink)" font-weight="400">xx %</text><text x="70" y="195" fill="var(--blue)">Data 1</text>
      <text x="206" y="227" fill="var(--ink)" font-weight="400">xx %</text><text x="206" y="235" fill="var(--navy)">Data 3</text>
      <text x="86" y="256" fill="var(--ink)" font-weight="400">xx %</text><text x="86" y="264" fill="var(--brown)">Data 5</text>
      <text x="168" y="266" fill="var(--ink)" font-weight="400">xx %</text><text x="168" y="274" fill="var(--slate)">Data 4</text>
    </g>
  </svg>
  <div class="brand brand-connect" style="left:0;right:0;text-align:center;top:22px;font-size:14px">Nestwise Connect</div>
  <h2 class="slide-title" style="position:absolute;left:0;right:0;top:46px;text-align:center;color:var(--orange);font-size:18px;line-height:21px">Transaction Management System<br>and Support Team</h2>
  <ul class="bullets">
    <li>NW manages all pre-qualified buyers via our NW Connect -Transaction Management System - from pre-approval issue to close</li>
    <li class="sub">NW Connect is currently creating a 20% faster time to get a buyer to contract with a 55% higher conversion rate to close with our Lending Partner. 90% of buyers close with the original lender assigned through both lead channels</li>
    <li class="sub">NW Connect will produce bi-weekly buyer updates to assigned LO or branch</li>
    <li class="sub">Specific Buying stage and substage insight/reporting available to LO</li>
    <li class="sub">Dedicated NW BEST team will manage all aspects of the transaction - phone calls, e-mails, SMS, scheduling and partner Real Estate Agent relationship</li>
    <li>NW has the ability to offset the Lending Partner's advertising spend through purchasing of pre-qualified buyer leads or lead acquisition reduction cost.</li>
  </ul>
</section>

<!-- Slide: partnership -->
<section class="slide slide-partnership">
  <div class="filled-art" style="left:305px;top:60px;width:260px;height:240px;border-radius:50%;background:radial-gradient(circle,#e9ecf2 35%,#dfe3ea 60%,#f6f7f9 72%)" role="img" aria-label="Illustration of a team celebrating around a large pie chart"></div>
  <svg class="deco" width="563" height="317" viewBox="0 0 563 317">
    <path d="M0 317 L0 290 C30 230 110 225 200 240 C300 258 400 215 480 240 C520 252 545 262 563 258 L563 317Z" fill="var(--orange)"/>
  </svg>
  <h2 class="slide-title" style="position:absolute;left:57px;top:36px;color:var(--orange);font-size:21px;line-height:22px">Real Value and<br>Real Partnership</h2>
  <div class="brand brand-protect" style="left:393px;top:44px;font-size:14px">Nestwise Protect</div>
  <ul class="bullets" style="--bullet:var(--blue)">
    <li>NW maintains the relationship with buyers and agents via an exclusive 2 year agreement</li>
    <li style="--bullet:var(--orange)">NW manages the home search process for all parties; which enables consistent communication</li>
    <li>NW uses preferred title companies for a smoother transaction</li>
    <li style="--bullet:var(--orange)">NW engages with all parties post closing and continues the relationship</li>
  </ul>
</section>

<!-- Slide: summary -->
<section class="slide slide-summary">
  <svg class="deco" width="563" height="317" viewBox="0 0 563 317">
    <path d="M0 55 C150 45 300 48 563 58 L563 317 L0 317Z" fill="var(--mist)"/>
    <g fill="#bcdcf1" opacity=".8"><circle cx="78" cy="113" r="8"/><circle cx="162" cy="106" r="6"/><circle cx="75" cy="198" r="9"/><circle cx="175" cy="205" r="12"/><circle cx="40" cy="215" r="3"/><circle cx="395" cy="290" r="7"/></g>
    <g stroke="#bcdcf1" stroke-width="2"><line x1="78" y1="113" x2="175" y2="205"/><line x1="162" y1="106" x2="75" y2="198"/></g>
    <path d="M490 150 C470 140 445 140 430 150 L430 165 C450 158 470 160 490 170Z" fill="#b9d2ec"/>
    <polygon points="520,130 535,170 490,168" fill="#a9c6ea"/>
    <g transform="rotate(-90 138 111)" fill="none" stroke-width="7">
      <circle cx="138" cy="111" r="16" pathLength="100" stroke="var(--orange)" stroke-dasharray="18 100"/>
      <circle cx="138" cy="111" r="16" pathLength="100" stroke="var(--navy)" stroke-dasharray="32 100" stroke-dashoffset="-18"/>
      <circle cx="138" cy="111" r="16" pathLength="100" stroke="var(--brown)" stroke-dasharray="5 100" stroke-dashoffset="-50"/>
      <circle cx="138" cy="111" r="16" pathLength="100" stroke="var(--slate)" stroke-dasharray="25 100" stroke-dashoffset="-55"/>
      <circle cx="138" cy="111" r="16" pathLength="100" stroke="var(--blue)" stroke-dasharray="20 100" stroke-dashoffset="-80"/>
    </g>
    <g transform="rotate(-90 211 139)" fill="none" stroke-width="12">
      <circle cx="211" cy="139" r="28" pathLength="100" stroke="var(--blue)" stroke-dasharray="10 100"/>
      <circle cx="211" cy="139" r="28" pathLength="100" stroke="var(--orange)" stroke-dasharray="4 100" stroke-dashoffset="-10"/>
      <circle cx="211" cy="139" r="28" pathLength="100" stroke="var(--navy)" stroke-dasharray="28 100" stroke-dashoffset="-14"/>
      <circle cx="211" cy="139" r="28" pathLength="100" stroke="var(--slate)" stroke-dasharray="20 100" stroke-dashoffset="-42"/>
      <circle cx="211" cy="139" r="28" pathLength="100" stroke="var(--brown)" stroke-dasharray="18 100" stroke-dashoffset="-62"/>
      <circle cx="211" cy="139" r="28" pathLength="100" stroke="var(--blue)" stroke-dasharray="20 100" stroke-dashoffset="-80"/>
    </g>
    <g class="chart-label" font-size="5" font-weight="600">
      <text x="96" y="83" font-weight="400">xx %</text><text x="96" y="89" fill="var(--blue)">Data 1</text>
      <text x="140" y="80" font-weight="400">xx %</text><text x="140" y="86" fill="var(--orange)">Data 2</text>
      <text x="155" y="114" font-weight="400">xx %</text><text x="155" y="120" fill="var(--navy)">Data 4</text>
      <text x="94" y="126" font-weight="400">xx %</text><text x="94" y="132" fill="var(--slate)">Data 3</text>
      <text x="136" y="133" font-weight="400">xx %</text><text x="136" y="139" fill="var(--brown)">Data 5</text>
      <text x="175" y="86" font-weight="400">xx %</text><text x="175" y="92" fill="var(--blue)">Data 1</text>
      <text x="242" y="95" font-weight="400">xx %</text><text x="242" y="101" fill="var(--orange)">Data 2</text>
      <text x="250" y="148" font-weight="400">xx %</text><text x="250" y="154" fill="var(--navy)">Data 3</text>
      <text x="152" y="167" font-weight="400">xx %</text><text x="152" y="173" fill="var(--brown)">Data 5</text>
      <text x="220" y="177" font-weight="400">xx %</text><text x="220" y="183" fill="var(--slate)">Data 4</text>
    </g>
    <circle cx="501" cy="254" r="38" fill="var(--gold)"/>
    <circle cx="501" cy="254" r="30" fill="#c98f28"/>
    <rect x="425" y="266" width="22" height="26" fill="var(--navy)"/>
  </svg>
  <div class="brand brand-connect" style="left:110px;top:20px;font-size:15px">Nestwise Connect</div>
  <div class="brand brand-direct" style="left:358px;top:20px;font-size:15px"><span class="brand-dot"></span>Nestwise Direct</div>
  <div class="browser" style="left:329px;top:78px;width:156px;height:116px">
    <div class="browser-bar"><i style="background:var(--purple)"></i><i style="background:var(--orange)"></i><i style="background:var(--blue)"></i></div>
    <div class="browser-url" style="font-size:3.8px">https://www.nestwiserealty.com/direct/</div>
    <div class="browser-map" style="top:22px" role="img" aria-label="Home search map with listing price pins and a sign-in panel"></div>
  </div>
  <h2 class="slide-title summary-title">Nestwise Realty Network</h2>
  <ul class="summary-list">
    <li>NW Crew - 9,000 NW Agents Nationwide</li>
    <li>NW Protect - 2-Year Buyer Protection and Service Level Agreement</li>
    <li>NW Connect - Transaction Management and Concierge System</li>
    <li>NW Reporting - Stage, Sub-Stage and Follow-up system</li>
    <li>NW Exchange - API and Integration Services</li>
    <li>NW Select - Realtor Panel and Retail Management</li>
    <li>NW Direct - Buyer Lead Generation Service</li>
  </ul>
</section>

</body>
</html>
```